Info Graphic

We’re looking for a graphic designer to create an infographic that visually communicates Terrafold Collective’s three-phase approach to vegetation management, specifically for high-risk assets like airports. The infographic should effectively tell the story of how our process improves sustainability, reduces costs, and enhances efficiency compared to conventional vegetation management practices.

Project Scope:
Objective:

Develop an engaging and professional infographic that illustrates the three key phases of Terrafold’s approach:
Phase 1 - Audit – Identifying existing vegetation and reviewing current management practices.
Phase 2 Work out a Program – Developing a site-specific plan to address identified issues and meet project KPIs. Matrix of options and budgets
Phase 3 Implementation, Monitoring & Assessment – Full program delivery, stakeholder engagement, project management. Monitor and assess the progress of the program, adjusting strategies as needed, and providing a final report for ongoing management.

Key Requirements:
The infographic should be visually compelling and easy to understand.
It should highlight the benefits of our approach (cost savings, environmental sustainability, efficiency).

The design should align with Terrafold Collective’s branding (colors, typography, style). I can provide some of our other design work so as it remains inline with our current branding options.

I've included the phase detail, an example of something we'd like as well as an example of our PPT.

```html
<!DOCTYPE html>
<html lang="en">
<head>
<meta charset="utf-8">
<title>Terrafold Collective – Three-Phase Approach</title>
<link rel="stylesheet" href="https://fonts.googleapis.com/css2?family=Poppins:wght@400;700;800&display=swap">
<style>
  :root {
    --green: #75bc43;
    --green-soft: #a9d67f;
    --green-pale: #d6ebc2;
    --white: #ffffff;
    --ink: #1f1f1f;
  }
  * { margin: 0; padding: 0; box-sizing: border-box; }
  html, body { width: 1200px; height: 786px; overflow: hidden; background: var(--white); }
  body { position: relative; font-family: "Poppins", sans-serif; }

  .header {
    position: absolute; left: 0; top: 0; width: 1200px; height: 96px;
    background: var(--green); display: flex; align-items: center; justify-content: center;
  }
  .header h1 {
    color: var(--white); font-weight: 800; font-size: 31px; letter-spacing: 0.2px; line-height: 1;
  }

  .phase {
    position: absolute; top: 166px; width: 286px; height: 389px;
    border: 5px solid var(--green); background: var(--white);
  }
  .phase--one { left: 64px; }
  .phase--two { left: 458px; background: var(--green); }
  .phase--three { left: 853px; }

  .phase__label {
    height: 29px; display: flex; align-items: center; justify-content: center;
    font-weight: 800; font-size: 14px; color: var(--green); background: var(--white);
  }
  .phase--two .phase__label { background: var(--green); color: var(--white); }

  .phase__title {
    height: 67px; display: flex; align-items: center; justify-content: center; text-align: center;
    background: var(--green); color: var(--white); font-weight: 800; font-size: 23px; line-height: 1.02;
  }
  .phase--two .phase__title { background: var(--white); color: var(--green); }

  .phase__band { height: 45px; background: var(--green-pale); }
  .phase--two .phase__band { background: var(--green-soft); }

  .phase__list { list-style: none; padding: 38px 0 0 12px; }
  .phase__list li {
    position: relative; padding-left: 28px; height: 21px; line-height: 21px;
    font-size: 15.5px; color: var(--ink); white-space: nowrap;
  }
  .phase__list li::before {
    content: ""; position: absolute; left: 0; top: 3px; width: 15px; height: 15px;
    border-radius: 50%; background: var(--green);
  }
  .phase--two .phase__list li { color: var(--white); }
  .phase--two .phase__list li::before { background: var(--white); }

  .flow-arrow { position: absolute; top: 361px; width: 75px; height: 64px; }
  .flow-arrow--one { left: 367px; }
  .flow-arrow--two { left: 761px; }

  .footer-band {
    position: absolute; left: 0; top: 630px; width: 1200px; height: 72px; background: var(--green-pale);
  }
  .footer {
    position: absolute; left: 0; top: 702px; width: 1200px; height: 84px; background: var(--green);
  }
  .footer__url {
    position: absolute; left: 81px; top: 26px; color: var(--white); font-size: 23px; font-weight: 400;
  }
  .brand {
    position: absolute; right: 80px; top: 24px; display: flex; align-items: center; gap: 12px;
  }
  .brand__dot { width: 30px; height: 30px; border-radius: 50%; background: var(--white); }
  .brand__name { color: var(--white); font-weight: 700; font-size: 28px; line-height: 1; }
</style>
</head>
<body>
  <header class="header">
    <h1>FIND A PROBLEM – QUANTIFY THE PROBLEM – SOLUTION</h1>
  </header>

  <section class="phase phase--one">
    <div class="phase__label">PHASE 1</div>
    <h2 class="phase__title">ASSESS + UNDERSTAND</h2>
    <div class="phase__band" role="img" aria-label="Diagonal hatch band"></div>
    <ul class="phase__list">
      <li>Site Audit</li>
      <li>Survey &amp; Mapping</li>
      <li>Agronomic Assessment</li>
      <li>Data Analysis</li>
      <li>Issue ID</li>
      <li>Report &amp; Recommendations</li>
      <li>Scorecard</li>
      <li>Risk Identification</li>
    </ul>
  </section>

  <svg class="flow-arrow flow-arrow--one" viewBox="0 0 75 64" aria-hidden="true">
    <polygon points="0,18 42,18 42,0 75,32 42,64 42,46 0,46" fill="#75bc43"/>
    <rect x="0" y="46" width="42" height="0" fill="#a9d67f"/>
    <polygon points="0,46 42,46 42,64 0,64" fill="#d6ebc2" transform="translate(0,-18)"/>
  </svg>

  <section class="phase phase--two">
    <div class="phase__label">PHASE 2</div>
    <h2 class="phase__title">SOLVE</h2>
    <div class="phase__band" role="img" aria-label="Diagonal hatch band"></div>
    <ul class="phase__list">
      <li>Program Options Matrix</li>
      <li>Multiyear Budget Forecast</li>
      <li>Stakeholder Engagement</li>
      <li>ID Guide</li>
      <li>Program Implementation</li>
      <li>Strategy</li>
      <li>Handbook</li>
      <li>Manual Guide</li>
    </ul>
  </section>

  <svg class="flow-arrow flow-arrow--two" viewBox="0 0 75 64" aria-hidden="true">
    <polygon points="0,18 42,18 42,0 75,32 42,64 42,46 0,46" fill="#75bc43"/>
    <polygon points="0,46 42,46 42,64 0,64" fill="#d6ebc2" transform="translate(0,-18)"/>
  </svg>

  <section class="phase phase--three">
    <div class="phase__label">PHASE 3</div>
    <h2 class="phase__title">GUIDE<br>MONITOR – EVALUATE</h2>
    <div class="phase__band" role="img" aria-label="Diagonal hatch band"></div>
    <ul class="phase__list">
      <li>Full Program</li>
      <li>Detailed Implementation</li>
      <li>Plan</li>
      <li>Training</li>
      <li>Stakeholder Management</li>
      <li>Project Management</li>
      <li>Delivery Support</li>
      <li>Scientific Monitoring</li>
    </ul>
  </section>

  <div class="footer-band" role="img" aria-label="Diagonal hatch band"></div>
  <footer class="footer">
    <span class="footer__url">www.terrafoldcollective.com.au</span>
    <div class="brand">
      <span class="brand__dot"></span>
      <span class="brand__name">Terrafold Collective</span>
    </div>
  </footer>
</body>
</html>
```